Business card for communications

Need a business card for my consulting business - I work with not for profits, start ups and social enterprises on their media, communications campaigns.

Please see my website for colours, images and fonts www.morvenquillet.example

Morven Quillet
Communications & Campaign strategist
Sydney - Melbourne
M: 0498 317 250
E: morven@morvenquillet.example
S: morvenquillet
W: morvenquillet.example
T: @morvenquillet

(above is info only and can be presented any way e.g. should not have to be M for mobile - it should be an icon)
Updates

Dear designers I have updated the brief and uploaded high res images from my website for you to use. The designs so far with the use of images and icons are much better so far. Thank you I look forward to receiving your revised designs. Morven Quillet

Industry/Entity Type

Communications

Font styles to use
Sans Serif

Requirements
Must have
• Icons for contact details
Images from the website www.morvenquillet.example
Nice to have
• Images - attached

```html
<!DOCTYPE html>
<html lang="en">
<head>
<meta charset="utf-8">
<title>Morven Quillet — Business Card</title>
<link rel="stylesheet" href="https://fonts.googleapis.com/css2?family=Arimo:wght@400;700&display=swap">
<style>
  :root {
    --bg: #3b3b3e;
    --yellow: #f7e01a;
    --black: #0c0c0c;
    --ink: #111111;
    --white: #ffffff;
    --photo-wood: #8a5a32;
    --photo-grey: #6f6a66;
  }
  * { box-sizing: border-box; margin: 0; padding: 0; }
  html, body {
    width: 1200px; height: 960px; overflow: hidden;
    background: var(--bg);
    font-family: "Arimo", Arial, sans-serif;
  }
  .stage { position: relative; width: 1200px; height: 960px; }
  .card {
    position: absolute; top: 150px;
    width: 400px; height: 660px;
    overflow: hidden;
    background: var(--yellow);
    box-shadow: 0 18px 40px rgba(0,0,0,.45);
  }
  .card--back { left: 140px; }
  .card--front { left: 660px; }

  /* back */
  .services { position: absolute; top: 0; left: 0; right: 0; height: 350px; padding: 44px 44px 0; }
  .services__title {
    display: flex; align-items: center; gap: 16px;
    font-size: 30px; font-weight: 400; letter-spacing: 1px; color: var(--ink);
    margin-bottom: 24px;
  }
  .services__plus { font-size: 36px; line-height: 1; font-weight: 700; }
  .services__list { list-style: none; }
  .services__item {
    display: flex; align-items: center; gap: 18px;
    font-size: 19px; color: var(--ink); height: 40px; margin-bottom: 14px;
  }
  .services__icon {
    width: 40px; height: 40px; border-radius: 50%;
    background: var(--white); flex: none;
    box-shadow: 0 1px 3px rgba(0,0,0,.15);
  }
  .team-photo {
    position: absolute; left: 0; right: 0; bottom: 0; height: 310px;
    background: radial-gradient(ellipse at 50% 45%, #a86d3c 0%, var(--photo-wood) 45%, #5a5450 100%);
  }

  /* front */
  .front__top { position: absolute; top: 0; left: 0; right: 0; height: 370px; background: var(--black); }
  .portrait {
    position: absolute; top: 36px; left: 72px; width: 256px; height: 256px;
    border: 3px solid var(--yellow);
    background: linear-gradient(160deg, #8d8884 0%, var(--photo-grey) 55%, #3f3a37 100%);
  }
  .name {
    position: absolute; top: 314px; left: 0; right: 0; text-align: center;
    color: var(--yellow); font-size: 30px; letter-spacing: 1px; font-weight: 400;
  }
  .contacts { position: absolute; top: 398px; left: 40px; right: 20px; list-style: none; }
  .contact {
    display: flex; align-items: center; gap: 18px;
    font-size: 18px; color: var(--ink); height: 40px;
  }
  .contact__icon {
    width: 30px; height: 30px; border-radius: 7px; background: var(--black);
    flex: none; display: flex; align-items: center; justify-content: center;
  }
  .contact__icon svg { width: 18px; height: 18px; }
</style>
</head>
<body>
<main class="stage">

  <section class="card card--back" aria-label="Card back">
    <div class="services">
      <h2 class="services__title"><span class="services__plus">+</span>SERVICES</h2>
      <ul class="services__list">
        <li class="services__item"><span class="services__icon" aria-hidden="true"></span>Communications Strategy</li>
        <li class="services__item"><span class="services__icon" aria-hidden="true"></span>Media Relations</li>
        <li class="services__item"><span class="services__icon" aria-hidden="true"></span>PR &amp; Campaigns</li>
        <li class="services__item"><span class="services__icon" aria-hidden="true"></span>Strategic Counsel</li>
      </ul>
    </div>
    <div class="team-photo" role="img" aria-label="Photo of a team working around a wooden table with laptops and papers"></div>
  </section>

  <section class="card card--front" aria-label="Card front">
    <div class="front__top">
      <div class="portrait" role="img" aria-label="Portrait photo of Morven Quillet"></div>
      <h1 class="name">MORVEN QUILLET</h1>
    </div>
    <ul class="contacts">
      <li class="contact">
        <span class="contact__icon"><svg viewBox="0 0 24 24"><path fill="#fff" d="M12 2a7 7 0 0 0-7 7c0 5 7 13 7 13s7-8 7-13a7 7 0 0 0-7-7zm0 9.5A2.5 2.5 0 1 1 12 6.5a2.5 2.5 0 0 1 0 5z"/></svg></span>
        Sydney - Melbourne
      </li>
      <li class="contact">
        <span class="contact__icon"><svg viewBox="0 0 24 24"><rect x="7" y="2" width="10" height="20" rx="2" fill="#fff"/><rect x="9" y="5" width="6" height="10" fill="#0c0c0c"/></svg></span>
        0498 317 250
      </li>
      <li class="contact">
        <span class="contact__icon"><svg viewBox="0 0 24 24"><rect x="3" y="6" width="18" height="12" fill="#fff"/><path d="M3 6l9 7 9-7" fill="none" stroke="#0c0c0c" stroke-width="1.6"/></svg></span>
        morven@morvenquillet.example
      </li>
      <li class="contact">
        <span class="contact__icon"><svg viewBox="0 0 24 24"><path fill="#fff" d="M4 4h16a1 1 0 0 1 1 1v11a1 1 0 0 1-1 1H10l-5 4v-4H4a1 1 0 0 1-1-1V5a1 1 0 0 1 1-1z"/></svg></span>
        morvenquillet
      </li>
      <li class="contact">
        <span class="contact__icon"><svg viewBox="0 0 24 24"><g fill="none" stroke="#fff" stroke-width="1.8"><circle cx="12" cy="12" r="9"/><path d="M3 12h18M12 3c3 3 3 15 0 18M12 3c-3 3-3 15 0 18"/></g></svg></span>
        morvenquillet.example
      </li>
      <li class="contact">
        <span class="contact__icon"><svg viewBox="0 0 24 24"><g fill="none" stroke="#fff" stroke-width="2" stroke-linecap="round"><circle cx="12" cy="12" r="3.5"/><path d="M15.5 9v4.5a2.5 2.5 0 0 0 5 0V12a8.5 8.5 0 1 0-3.5 6.9"/></g></svg></span>
        @morvenquillet
      </li>
    </ul>
  </section>

</main>
</body>
</html>
```